Ridgely Forge business card for handing simple contact information and generating service awareness

Utilizing the attached logo(s), generate a professional, but approachable, card conveying a sense of capability and integrity. Please only use one logo of the four attached; the different colors are all acceptable, but preference will be given to a design integrating a teal/turquoise logo,

I do not know where to put in the contact information or details?

Target Market(s)

Agriculture, Farming, Timber, Forestry, Construction, Crane Service

Industry/Entity Type

Contact Information for Business Card

Name, Phone Number, email address

Colors

Designer to choose colors to be used in the design.

Requirements
Nice to have
• It would be great to have either a mountain or one of the attached cranes as a backdrop on the rear of the card. Simple watermarks and/or Debossing is also great

```html
<!DOCTYPE html>
<html lang="en">
<head>
<meta charset="utf-8">
<title>Ridgely Forge – Business Card</title>
<link href="https://fonts.googleapis.com/css2?family=Open+Sans:wght@400;600;700&display=swap" rel="stylesheet">
<style>
  :root {
    --backdrop: #232323;
    --card-dark: #1f1f22;
    --card-dark-end: #232a29;
    --teal: #2b7566;
    --teal-light: #3a8f7e;
    --teal-deep: #1e5a4e;
    --ink-light: #f2f2f2;
    --rule: #c9c9c9;
  }
  * { box-sizing: border-box; margin: 0; padding: 0; }
  html, body {
    width: 1200px; height: 780px; overflow: hidden;
    background: var(--backdrop);
    font-family: "Open Sans", Arial, sans-serif;
  }
  .stage {
    position: relative; width: 1200px; height: 780px;
    display: flex; align-items: center; justify-content: center; gap: 48px;
  }
  .card {
    position: relative; width: 540px; height: 309px;
    border-radius: 3px; overflow: hidden;
    box-shadow: 0 18px 40px rgba(0,0,0,.45);
  }

  /* Front */
  .card-front {
    background: linear-gradient(160deg, var(--card-dark) 0%, var(--card-dark) 55%, var(--card-dark-end) 100%);
    color: var(--ink-light);
  }
  .watermark-area {
    position: absolute; right: -40px; bottom: -70px; width: 340px; height: 280px;
    border-radius: 50%;
    background: radial-gradient(circle at 50% 45%, rgba(43,117,102,.22), rgba(43,117,102,.06) 65%, transparent 75%);
  }
  .brand {
    position: absolute; left: 38px; top: 44px;
    display: flex; align-items: center; gap: 12px;
  }
  .brand-dot {
    width: 40px; height: 40px; border-radius: 50%; background: var(--teal);
  }
  .brand-name {
    font-size: 27px; font-weight: 700; color: var(--teal);
    text-transform: uppercase; letter-spacing: .5px;
  }
  .divider {
    position: absolute; left: 262px; top: 96px;
  }
  .person {
    position: absolute; left: 300px; top: 100px;
  }
  .person-name {
    font-size: 27px; font-weight: 700; color: var(--teal); line-height: 1.1;
  }
  .person-title {
    font-size: 14px; font-weight: 600; margin-top: 4px;
  }
  .contacts {
    list-style: none; margin-top: 14px;
  }
  .contacts li {
    display: flex; align-items: center; gap: 8px;
    font-size: 13px; line-height: 1.7;
  }
  .contacts svg { width: 12px; height: 12px; fill: var(--teal-light); flex: none; }
  .address {
    position: absolute; left: 38px; bottom: 26px;
    font-size: 13px;
  }

  /* Back */
  .card-back {
    background: var(--teal);
    display: flex; align-items: center; justify-content: center;
  }
  .pattern-area {
    position: absolute; inset: 0;
    background: linear-gradient(135deg, var(--teal) 0%, #2e7a6b 60%, var(--teal-light) 100%);
  }
  .back-brand {
    position: relative; display: flex; align-items: center; gap: 8px;
    margin-top: 150px; margin-left: 90px;
  }
  .back-brand .brand-dot { width: 18px; height: 18px; background: #ffffff; }
  .back-brand .brand-name { font-size: 13px; color: #ffffff; }
</style>
</head>
<body>
<main class="stage">
  <section class="card card-front" aria-label="Business card front">
    <div class="watermark-area" role="img" aria-label="Faint large brand emblem watermark"></div>

    <div class="brand">
      <span class="brand-dot"></span>
      <span class="brand-name">Ridgely Forge</span>
    </div>

    <svg class="divider" width="30" height="100" viewBox="0 0 30 100" aria-hidden="true">
      <line x1="29" y1="0" x2="1" y2="100" stroke="var(--rule)" stroke-width="1"/>
    </svg>

    <div class="person">
      <h1 class="person-name">Dalen Varga</h1>
      <p class="person-title">Managing Director</p>
      <ul class="contacts">
        <li>
          <svg viewBox="0 0 24 24" aria-hidden="true"><path d="M6.6 10.8a15.1 15.1 0 0 0 6.6 6.6l2.2-2.2a1 1 0 0 1 1-.25 11.4 11.4 0 0 0 3.6.57 1 1 0 0 1 1 1V20a1 1 0 0 1-1 1A17 17 0 0 1 3 4a1 1 0 0 1 1-1h3.5a1 1 0 0 1 1 1c0 1.25.2 2.45.57 3.57a1 1 0 0 1-.25 1z"/></svg>
          (555) 014-2290
        </li>
        <li>
          <svg viewBox="0 0 24 24" aria-hidden="true"><path d="M2 5h20v14H2zm2 2v.5l8 5 8-5V7l-8 5z"/></svg>
          hello@ridgelyforge.com
        </li>
        <li>
          <svg viewBox="0 0 24 24" aria-hidden="true"><path d="M12 2a10 10 0 1 0 0 20 10 10 0 0 0 0-20zm6.9 6h-3a15 15 0 0 0-1.3-3.9A8 8 0 0 1 18.9 8zM12 4c.8 1.2 1.5 2.5 1.9 4h-3.8c.4-1.5 1.1-2.8 1.9-4zM4.3 14a8 8 0 0 1 0-4h3.4a16 16 0 0 0 0 4zm.8 2h3a15 15 0 0 0 1.3 3.9A8 8 0 0 1 5.1 16zm3-8h-3a8 8 0 0 1 4.3-3.9A15 15 0 0 0 8.1 8zM12 20c-.8-1.2-1.5-2.5-1.9-4h3.8c-.4 1.5-1.1 2.8-1.9 4zm2.3-6H9.7a14 14 0 0 1 0-4h4.6a14 14 0 0 1 0 4zm.3 5.9a15 15 0 0 0 1.3-3.9h3a8 8 0 0 1-4.3 3.9zM16.3 14a16 16 0 0 0 0-4h3.4a8 8 0 0 1 0 4z"/></svg>
          www.ridgelyforge.com
        </li>
      </ul>
    </div>

    <p class="address">418 Cedar Hollow Rd. Suite 12 Millbrook, TX 76999</p>
  </section>

  <section class="card card-back" aria-label="Business card back">
    <div class="pattern-area" role="img" aria-label="Debossed repeating brand emblem pattern on teal"></div>
    <div class="back-brand">
      <span class="brand-dot"></span>
      <span class="brand-name">Ridgely Forge</span>
    </div>
  </section>
</main>
</body>
</html>
```